Tallyden Web Design

Create Website Design for Tallyden. Tallyden is online application for collaboration team work system (task list management). More concept design for this project please find attach file ("tallyden website concept.pdf") . But my concept is just describe minimal features not bind design

For tallyden logo, i had already attach files. But i had not decided what color i chose, so it's okay if you suggest logo color for your suitable website design.
Updates

Dear All Designer,

I like brisk carousel (http://quillforge-labs.example/brisk-carousel/),
may be your concept design can adjust with this concept.
but don't worry about script for brisk carousel, my team will be handle
You just make website design to suitable with brisk carousel

but if you had own website design concept are welcome

thanks

Target Market(s)

Business Company

Industry/Entity Type

Management

```html
<!DOCTYPE html>
<html lang="en">
<head>
<meta charset="utf-8">
<title>Tallyden — Online Collaboration Team Work</title>
<link href="https://fonts.googleapis.com/css2?family=Questrial&family=Roboto+Condensed:wght@400&display=swap" rel="stylesheet">
<style>
:root{
  --header-bg:#1d1d1d;
  --header-bg-dark:#151515;
  --nav-bg:#121212;
  --nav-divider:#333;
  --nav-text:#d8d8d8;
  --accent:#17a9cc;
  --accent-deep:#1a7f95;
  --teal-btn-top:#3a95a8;
  --teal-btn-bottom:#1d6676;
  --light-text:#ececec;
  --band-bg:#e3e9e9;
  --heading:#222;
  --footer-bg:#ffffff;
  --body-text:#4a4a4a;
  --rule:#d6d6d6;
  --icon:#6a6a6a;
}
*{margin:0;padding:0;box-sizing:border-box}
html,body{width:1200px;height:985px;overflow:hidden;background:var(--footer-bg)}
body{font-family:"Questrial",sans-serif;position:relative}

.site-header{position:absolute;left:0;top:0;width:1200px;height:548px;
  background:radial-gradient(ellipse at 40% 30%,#262626 0%,var(--header-bg) 45%,var(--header-bg-dark) 100%);
  border-bottom:1px solid #0b0b0b}
.header-arc{position:absolute;left:0;top:0}
.brand{position:absolute;left:110px;top:14px;display:flex;align-items:center;gap:10px;
  font-family:"Questrial",sans-serif;font-size:50px;color:var(--accent-deep);letter-spacing:-1px;line-height:60px}
.brand-dot{width:22px;height:22px;border-radius:50%;background:var(--accent)}
.login-btn{position:absolute;left:980px;top:32px;width:80px;height:30px;border-radius:15px;
  background:linear-gradient(#26bce0,#0d93b7);border:1px solid #0a6f8b;color:#0c2a33;
  font-size:15px;text-align:center;line-height:28px}

.main-nav{position:absolute;left:108px;top:90px;width:970px;height:44px;background:var(--nav-bg);
  border-radius:8px;display:flex;align-items:center;padding-left:0}
.main-nav a{color:var(--nav-text);text-decoration:none;font-size:15px;padding:0 26px;
  border-right:1px solid var(--nav-divider);line-height:22px}
.main-nav a:last-child{border-right:none}
.main-nav a.is-active{color:var(--accent);padding-left:23px}
.nav-marker{position:absolute;left:126px;top:130px;width:52px;height:8px;border-radius:0 0 26px 26px;background:var(--accent-deep)}

.hero-media{position:absolute;left:108px;top:173px;width:560px;height:335px;border-radius:10px;
  border:3px solid #000;box-shadow:0 0 0 1px #3a3a3a;
  background:linear-gradient(135deg,#eef0f2 0%,#d9dde2 40%,#3a3f4b 70%,#e6e8ea 100%);overflow:hidden}
.play-btn{position:absolute;left:250px;top:137px}

.hero-copy{position:absolute;left:737px;top:212px}
.hero-title{font-size:54px;color:var(--light-text);line-height:60px;font-weight:400}
.hero-sub{font-size:54px;color:var(--accent);line-height:70px}
.hero-tag{font-size:24px;color:var(--accent);margin-top:4px;letter-spacing:.3px}
.cta{position:absolute;left:737px;top:405px;width:178px;height:47px;border-radius:16px;
  background:linear-gradient(var(--teal-btn-top),var(--teal-btn-bottom));border:1px solid #0c3f4a;
  color:#f2f2f2;font-size:22px;text-align:center;line-height:45px;text-shadow:0 1px 1px #000}
.cta-reflection{position:absolute;left:740px;top:453px;width:172px;height:18px;border-radius:0 0 14px 14px;
  background:linear-gradient(rgba(40,110,125,.45),rgba(40,110,125,0))}

.features{position:absolute;left:0;top:549px;width:1200px;height:268px;background:var(--band-bg)}
.feature{position:absolute;top:35px;width:298px}
.feature h2{font-weight:400;font-size:23px;color:var(--heading);height:44px}
.feature-media{width:298px;height:139px;border-radius:8px;border:1px solid #b9bfbf}
.feature-apps{background:linear-gradient(120deg,#3a3a3a,#8a8a8a 50%,#d5d5d5)}
.feature-sync{background:linear-gradient(160deg,#ffffff,#dfeef6 55%,#9fcbe2)}
.feature-report{background:linear-gradient(135deg,#e9e9ee,#b9b6e0 45%,#2b2b2b 85%)}

.zigzag{position:absolute;left:0;top:806px}

.intro{position:absolute;left:108px;top:848px;width:970px;font-family:"Roboto Condensed",sans-serif;
  font-size:13.5px;line-height:20px;color:var(--body-text);text-align:justify}
.footer-rule{position:absolute;left:110px;top:915px;width:958px;height:1px;background:var(--rule)}
.footer-links{position:absolute;left:112px;top:935px;font-family:"Roboto Condensed",sans-serif;font-size:13px;color:#111}
.footer-links a{color:#111;text-decoration:none}
.social{position:absolute;left:886px;top:936px;display:flex;gap:4px}
.social span{width:16px;height:16px;border-radius:2px;background:var(--icon)}
.copyright{position:absolute;left:960px;top:936px;font-family:"Roboto Condensed",sans-serif;font-size:12.5px;color:#555}
</style>
</head>
<body>
<header class="site-header">
  <svg class="header-arc" width="1200" height="548" aria-hidden="true">
    <path d="M480 0 C560 120 560 380 420 548" fill="none" stroke="#2a2a2a" stroke-width="40"/>
  </svg>
  <div class="brand"><span>tallyden</span><span class="brand-dot"></span></div>
  <div class="login-btn">LOGIN</div>

  <nav class="main-nav">
    <a class="is-active" href="#">HOME</a>
    <a href="#">SOLUTIONS</a>
    <a href="#">TEAM WORK</a>
    <a href="#">APPLICATION</a>
    <a href="#">REPORT</a>
    <a href="#">ABOUT US</a>
    <a href="#">NEWS</a>
    <a href="#">CONTACT US</a>
  </nav>
  <div class="nav-marker"></div>

  <div class="hero-media" role="img" aria-label="Photo of three colleagues reviewing documents together at an office desk">
    <svg class="play-btn" width="60" height="60" aria-hidden="true">
      <circle cx="30" cy="30" r="28" fill="#3cb6ea" stroke="#e9f6fc" stroke-width="3"/>
      <path d="M23 17 L43 30 L23 43 Z" fill="#ffffff"/>
    </svg>
  </div>

  <div class="hero-copy">
    <h1 class="hero-title">CUSTOMIZE</h1>
    <div class="hero-sub">ONLINE</div>
    <div class="hero-tag">COLLABORATION TEAM WORK</div>
  </div>
  <div class="cta">GET STARTED</div>
  <div class="cta-reflection"></div>
</header>

<section class="features">
  <div class="feature" style="left:108px">
    <h2>Customize Application</h2>
    <div class="feature-media feature-apps" role="img" aria-label="Photo of a person holding a tablet with floating application windows"></div>
  </div>
  <div class="feature" style="left:448px">
    <h2>Synchronize All Device</h2>
    <div class="feature-media feature-sync" role="img" aria-label="Illustration of cloud storage connected to computers and devices"></div>
  </div>
  <div class="feature" style="left:788px">
    <h2>Report</h2>
    <div class="feature-media feature-report" role="img" aria-label="Photo of project charts, a calculator and a laptop on a desk"></div>
  </div>
</section>

<svg class="zigzag" width="1200" height="12" aria-hidden="true">
  <defs>
    <pattern id="teeth" width="14" height="12" patternUnits="userSpaceOnUse">
      <path d="M0 0 H14 V4 L7 11 L0 4 Z" fill="#e3e9e9"/>
    </pattern>
  </defs>
  <rect width="1200" height="12" fill="url(#teeth)"/>
</svg>

<p class="intro">There are many variations of passages of Lorem Ipsum available, but the majority have suffered alteration in some form, by injected humour, or randomised words which don't look even slightly believable. If you are going to use a passage of Lorem Ipsum..</p>
<div class="footer-rule"></div>
<div class="footer-links"><a href="#">Home</a> | <a href="#">Solutions</a> | <a href="#">Team Work</a> | <a href="#">Application</a> | <a href="#">Report</a> | <a href="#">About Us</a> | <a href="#">News</a> | <a href="#">Contact Us</a></div>
<div class="social" aria-label="Social links"><span></span><span></span><span></span></div>
<div class="copyright">Tallyden © 2013</div>
</body>
</html>
```